FernPath Promotions Flyer Design

I need to be able to have a flyer that shows what I do for businesses. Same logo that you designed.

Requirements
Must have
• I gave an example of what I need it to say in the attachment. Must have logo and resemble business card style.
Nice to have
• It could include pictures of what a digital sign is. We offer an KVTA, weather, and news slide on our advertising. I included sample pictures of those.

```html
<!DOCTYPE html>
<html lang="en">
<head>
<meta charset="utf-8">
<title>FernPath Promotions Flyer</title>
<link href="https://fonts.googleapis.com/css2?family=Archivo+Black&family=Arimo:ital,wght@0,400;0,700;1,700&family=Roboto:wght@700&display=swap" rel="stylesheet">
<style>
  :root {
    --green: #8cc63f;
    --grey: #666666;
    --text-grey: #555555;
    --backdrop: #231f20;
    --label: #3f3b3c;
    --yellow: #f7e600;
    --white: #ffffff;
    --black: #0a0a0a;
  }
  * { margin: 0; padding: 0; box-sizing: border-box; }
  html, body { width: 1200px; height: 2321px; overflow: hidden; background: var(--backdrop); }
  .sheet {
    position: absolute; left: 0; top: 0;
    width: 1225px; height: 2369px;
    transform: scale(0.98); transform-origin: 0 0;
    font-family: "Arimo", Arial, sans-serif;
  }
  .side-label {
    position: absolute; left: 0; width: 1225px; text-align: center;
    font-family: "Archivo Black", sans-serif; font-size: 34px; color: var(--label);
  }
  .side-label.front { top: 124px; }
  .side-label.back { top: 2222px; }
  .panel {
    position: absolute; left: 226px; width: 773px; height: 1000px;
    background: var(--white); overflow: hidden;
  }
  .panel.front { top: 172px; }
  .panel.back { top: 1197px; }
  .panel svg.shapes { position: absolute; left: 0; top: 0; width: 773px; height: 1000px; }
  .venue-photo {
    position: absolute; left: 0; top: 170px; width: 773px; height: 640px;
    background:
      radial-gradient(ellipse 230px 130px at 395px 175px, #6f9fd6 0%, #5a86b8 60%, rgba(90,120,160,0) 100%),
      linear-gradient(180deg, #a5564a 0%, #8f4a40 45%, #5a3229 80%, #2e211d 100%);
  }
  .brand {
    position: absolute; display: flex; align-items: center; gap: 10px;
    font-family: "Archivo Black", sans-serif; color: var(--grey);
  }
  .brand-mark { width: 14px; height: 14px; border-radius: 50%; background: var(--green); }
  .brand-name { display: flex; flex-direction: column; line-height: 1; }
  .brand-name .word { font-size: 58px; letter-spacing: -1px; }
  .brand-name .sub { font-size: 17px; letter-spacing: 9px; margin-top: 4px; }
  .front .brand { left: 222px; top: 82px; }
  .back .brand { left: 107px; top: 58px; }
  .back .brand .word { font-size: 50px; }
  .back .brand .sub { font-size: 15px; letter-spacing: 8px; }
  .headline {
    position: absolute; left: 0; top: 684px; width: 773px; text-align: center;
    font-family: "Archivo Black", sans-serif; font-size: 55px; line-height: 45px; color: var(--black);
  }
  .pitch {
    position: absolute; left: 120px; top: 830px; width: 533px; text-align: center;
    font-family: "Roboto", sans-serif; font-weight: 700; font-size: 24px; line-height: 26.5px; color: var(--white);
  }
  .section-title {
    position: absolute; left: 104px;
    font-family: "Archivo Black", sans-serif; color: var(--green); font-size: 31px; line-height: 26px;
  }
  .section-title.what { top: 174px; }
  .section-title.benefits { top: 318px; }
  .section-title.process { top: 656px; color: var(--white); }
  .bullets {
    position: absolute; left: 106px; width: 580px; list-style: none;
    font-size: 14.2px; line-height: 18px; color: var(--text-grey);
  }
  .bullets li { position: relative; padding-left: 15px; }
  .bullets li::before {
    content: ""; position: absolute; left: 0; top: 3px;
    width: 11px; height: 11px; border-radius: 50%; background: var(--green);
  }
  .bullets .strong { font-weight: 700; }
  .bullets.what { top: 206px; }
  .bullets.benefits { top: 377px; }
  .process-steps {
    position: absolute; left: 107px; top: 695px; width: 590px;
    font-size: 14.2px; line-height: 20.2px; color: var(--white);
  }
  .process-steps b { font-weight: 700; }
  .process-steps .note { font-weight: 700; font-style: italic; }
  .signup {
    position: absolute; left: 254px; top: 885px;
    font-family: "Archivo Black", sans-serif; font-size: 37px; color: var(--yellow);
  }
  .payline {
    position: absolute; left: 0; width: 773px; text-align: center;
    font-size: 16.5px; color: var(--white);
  }
  .payline.amount { top: 936px; left: -5px; }
  .payline.call { top: 963px; left: -31px; }
</style>
</head>
<body>
<div class="sheet">
  <div class="side-label front">FRONT</div>

  <section class="panel front">
    <div class="venue-photo" role="img" aria-label="Photo of people in a brick-walled lounge watching a wall-mounted digital sign showing a news ticker, with smaller sports screens beside it"></div>
    <svg class="shapes" viewBox="0 0 773 1000" aria-hidden="true">
      <path d="M0,0 H773 V230 Q560,182 320,188 Q140,192 0,200 Z" fill="var(--white)"/>
      <path d="M517,37 Q660,28 773,0 V26 Q650,52 517,37 Z" fill="var(--green)"/>
      <path d="M0,730 Q260,615 773,578 V1000 H0 Z" fill="var(--green)"/>
      <path d="M773,768 Q705,890 614,1000 H773 Z" fill="var(--grey)"/>
      <path d="M0,1000 Q110,960 232,953 Q130,968 60,1000 Z" fill="var(--grey)"/>
    </svg>
    <div class="brand">
      <div class="brand-name"><span class="word">FernPath</span><span class="sub">PROMOTIONS</span></div>
      <span class="brand-mark"></span>
    </div>
    <h1 class="headline">NEED EXTRA<br>MONEY FOR<br>YOUR BUSINESS?</h1>
    <p class="pitch">We provide monthly payments to businesses for allowing us to advertise local businesses on a TV screen in your place of business.</p>
  </section>

  <section class="panel back">
    <svg class="shapes" viewBox="0 0 773 1000" aria-hidden="true">
      <path d="M517,37 Q660,28 773,0 V26 Q650,52 517,37 Z" fill="var(--green)"/>
      <path d="M0,700 Q250,592 773,575 V1000 H0 Z" fill="var(--grey)"/>
      <path d="M773,780 Q700,900 604,1000 H773 Z" fill="var(--green)"/>
      <path d="M0,1000 V962 Q120,920 246,918 Q115,942 62,1000 Z" fill="var(--green)"/>
    </svg>
    <div class="brand">
      <div class="brand-name"><span class="word">FernPath</span><span class="sub">PROMOTIONS</span></div>
      <span class="brand-mark"></span>
    </div>

    <h2 class="section-title what">WHAT WE DO</h2>
    <ul class="bullets what">
      <li>We provide monthly payments to businesses for allowing us to advertise local businesses on a TV screen in your place of business.</li>
      <li>We provide the TV screen if you prefer (professional installation on our dime)</li>
      <li>We provide a win/win for the businesses that partner with us. Our business partners get paid to support local businesses.</li>
    </ul>

    <h2 class="section-title benefits">BENEFITS OF PARTNERING<br>with FernPath Promotions</h2>
    <ul class="bullets benefits">
      <li>WE PAY YOU!</li>
      <li>We advertise local businesses and business owners. We encourage them to stop by your establishment to check out their ad. This will create more foot traffic to your business.</li>
      <li>Waiting Rooms: Studies show perceived wait time can be decreased by up to 33% when there is digital signage present. This can make your clients’ 60 min wait feel like a 40 min wait.</li>
      <li>Professional ticker at the bottom of the digital design can display sports updates, breaking news, and weather. Our design approach makes your business look more professional.</li>
      <li class="strong">DID WE MENTION THAT WE PAY YOU?!!!</li>
    </ul>

    <h2 class="section-title process">EFFORTLESS PROCESS</h2>
    <div class="process-steps">
      <p><b>Day 1:</b> Sign on to partner with FernPath Promotions.</p>
      <p><b>Week 1:</b> We install a HDMI/USB drive to the screen. Our onsite time for this is less than 10 minutes and this WILL NOT disrupt your business operations. In fact, you may not even notice we came and went. (We can use an existing screen or install a new screen at no cost to you if space permits)</p>
      <p><b>Week 1-8:</b> We will be loading our local advertisers’ professional designs to the screen. (This is done remotely and does not require us to come in)</p>
      <p><b>End of 2nd Full Month:</b> Process is complete, and you will be receiving monthly checks!</p>
      <p class="note">Notice your involvement is only in the first and last step.</p>
    </div>
    <p class="signup">Sign-up. Get Paid.</p>
    <p class="payline amount">We will pay you ____________ each month.</p>
    <p class="payline call">Call for details_________________________.</p>
  </section>

  <div class="side-label back">BACK</div>
</div>
</body>
</html>
```